Dishcart

App Design for a an application on which you can order take aways from restaurants close to you.
(similar app : https://appvault.example/lu/app/brunomeal-pizza-burger-sushi/id538216047?l=en&mt=8 )

Logo is a taxi (psd of taxi an font attached)

Attached a draft mockup showing the screens needed.

Screens needed :

1. Splash Screen
2. Select you restaurant screen
3. Select your dish (meat, pizza, pasta....)
4. Select your extras (exta cheese, garlik etc...)
5. Exit screen with total amount and confirmation
6. Subscribe Screen where people have to register the first time.

Target Market(s)

age 14-54

Industry/Entity Type

Restaurant

Requirements
Must have
• Wood elements

```html
<!DOCTYPE html>
<html lang="fr">
<head>
<meta charset="utf-8">
<title>Dishcart – écrans</title>
<link href="https://fonts.googleapis.com/css2?family=Roboto+Condensed:wght@400;700&family=Roboto:wght@400;700&display=swap" rel="stylesheet">
<style>
  :root{
    --page:#2a1d14;
    --wood-dark:#3b2516;
    --wood-mid:#6b4529;
    --wood-light:#8a5c38;
    --seam:rgba(20,10,4,.55);
    --yellow:#f2d21a;
    --yellow-deep:#d9b300;
    --yellow-text:#5a4a00;
    --ink:#1c1c1c;
    --muted:#6d6d6d;
    --white:#ffffff;
    --row:#f1f1f1;
    --bar:#0d0d0d;
    --olive:#8a7300;
  }
  *{box-sizing:border-box;margin:0;padding:0}
  html,body{width:1200px;height:1040px;overflow:hidden;background:var(--page)}
  body{position:relative;font-family:"Roboto Condensed",Arial,sans-serif}
  .screen{
    position:absolute;top:165px;width:400px;height:710px;overflow:hidden;
    background:
      repeating-linear-gradient(90deg,transparent 0 56px,var(--seam) 56px 58px),
      radial-gradient(ellipse at 50% 35%,var(--wood-light),var(--wood-mid) 55%,var(--wood-dark));
    box-shadow:0 20px 50px rgba(0,0,0,.6);
  }
  .screen--home{left:150px}
  .screen--search{left:650px}
  .status{
    position:absolute;top:0;left:0;right:0;height:25px;background:rgba(0,0,0,.85);
    color:var(--white);font:700 13px "Roboto",Arial,sans-serif;
    display:flex;align-items:center;justify-content:space-between;padding:0 8px;
  }
  .status__time{position:absolute;left:0;right:0;text-align:center}
  .status__battery{width:22px;height:10px;border:1px solid var(--white);border-radius:2px;background:var(--white)}
  .brand{position:absolute;top:88px;left:0;right:0;text-align:center;
    font:700 30px "Roboto Condensed",Arial,sans-serif;color:#111}
  .hero{position:absolute;left:72px;top:155px;width:256px;height:190px;border-radius:24px;
    background:radial-gradient(ellipse at 50% 55%,#f0c020,#b98a10 55%,rgba(90,60,20,0) 75%)}
  .pick{position:absolute;left:26px;width:348px;height:74px;
    background:linear-gradient(var(--yellow),var(--yellow-deep));
    border:1px solid #b09000;box-shadow:0 4px 8px rgba(0,0,0,.45);
    display:flex;align-items:center;padding:0 16px;color:var(--yellow-text)}
  .pick--first{top:416px}.pick--second{top:509px}
  .pick__name{font-weight:700;font-size:25px;flex:1}
  .pick__kind{font-size:15px;margin-right:14px}
  .tabbar{position:absolute;left:0;right:0;bottom:0;height:92px;
    border-top:3px solid var(--yellow);background:var(--bar);display:flex}
  .tab{flex:1;display:flex;flex-direction:column;align-items:center;justify-content:center;gap:6px;
    color:var(--white);font:700 15px "Roboto",Arial,sans-serif;position:relative;
    background:linear-gradient(rgba(80,55,35,.85),rgba(45,30,18,.95));border-left:2px solid #000}
  .tab:first-child{border-left:0}
  .tab--active{background:#141414;color:var(--yellow)}
  .tab__badge{position:absolute;top:18px;left:78px;background:var(--yellow);color:#000;
    font-size:10px;padding:1px 3px;border-radius:2px}
  .radius{position:absolute;left:16px;top:41px;width:375px;height:104px;
    background:linear-gradient(#fafafa,#e4e4e4);border-radius:4px;box-shadow:0 3px 8px rgba(0,0,0,.4)}
  .radius__label{position:absolute;left:15px;top:20px;font-size:15px;color:var(--olive)}
  .radius__track{position:absolute;left:18px;right:18px;top:68px;height:8px;border-radius:4px;background:#d6d6d6;box-shadow:inset 0 1px 2px rgba(0,0,0,.3)}
  .radius__fill{width:56%;height:100%;border-radius:4px;background:var(--yellow)}
  .radius__knob{position:absolute;left:calc(56% - 10px);top:-6px;width:20px;height:20px;border-radius:50%;background:var(--yellow-deep);border:1px solid #b09000}
  .venue{position:absolute;left:16px;width:375px;height:61px;background:linear-gradient(var(--white),var(--row));
    box-shadow:0 3px 6px rgba(0,0,0,.45);display:flex;align-items:center;padding-left:5px}
  .venue__thumb{width:57px;height:50px;margin-right:16px;border:2px solid #fff;box-shadow:0 0 2px rgba(0,0,0,.5)}
  .venue__text{flex:1}
  .venue__name{font-weight:700;font-size:19px;color:var(--ink);line-height:1.05}
  .venue__kind{font-size:12px;color:var(--muted)}
  .venue__go{margin-right:16px}
</style>
</head>
<body>

<section class="screen screen--home">
  <div class="status"><span>▮▮▮ Nordel</span><span class="status__time">4:20 PM</span><span class="status__battery"></span></div>
  <div class="brand">Dishcart</div>
  <div class="hero" role="img" aria-label="Illustration d'un taxi jaune ancien"></div>
  <div class="pick pick--first"><span class="pick__name">La Pizza</span><span class="pick__kind">Italien</span>
    <svg width="14" height="18" viewBox="0 0 14 18"><path d="M2 2l9 7-9 7" fill="none" stroke="#5a4a00" stroke-width="4"/></svg></div>
  <div class="pick pick--second"><span class="pick__name">Chin Hong</span><span class="pick__kind">Chinnois</span>
    <svg width="14" height="18" viewBox="0 0 14 18"><path d="M2 2l9 7-9 7" fill="none" stroke="#5a4a00" stroke-width="4"/></svg></div>
  <nav class="tabbar">
    <div class="tab"><svg width="30" height="30" viewBox="0 0 30 30" fill="none" stroke="currentColor" stroke-width="2"><circle cx="18" cy="11" r="8"/><path d="M12 17L4 26"/></svg>Chercher</div>
    <div class="tab"><svg width="34" height="30" viewBox="0 0 34 30" fill="none" stroke="currentColor" stroke-width="2"><path d="M5 18a12 10 0 0 1 24 0zM2 21h30M17 6v2"/></svg>Commandes<span class="tab__badge">+2</span></div>
    <div class="tab"><svg width="30" height="30" viewBox="0 0 30 30" fill="none" stroke="currentColor" stroke-width="2"><rect x="4" y="6" width="22" height="19" rx="3"/><path d="M4 12h22M18 17h5"/></svg>Compte</div>
  </nav>
</section>

<section class="screen screen--search">
  <div class="status"><span>▮▮▮ Nordel</span><span class="status__time">4:20 PM</span><span class="status__battery"></span></div>
  <div class="radius">
    <div class="radius__label">12 restaurants dans mon environement</div>
    <div class="radius__track"><div class="radius__fill"></div><div class="radius__knob"></div></div>
  </div>

  <div class="venue" style="top:168px"><div class="venue__thumb" role="img" aria-label="Photo de vin et fromage" style="background:linear-gradient(135deg,#3a2a1c,#9b7a3a)"></div><div class="venue__text"><div class="venue__name">Dolce Maria</div><div class="venue__kind">Italien</div></div><svg class="venue__go" width="12" height="18" viewBox="0 0 12 18"><path d="M2 2l8 7-8 7" fill="none" stroke="#999" stroke-width="3"/></svg></div>
  <div class="venue" style="top:244px"><div class="venue__thumb" role="img" aria-label="Photo d'un hamburger" style="background:linear-gradient(#c98a3a,#7a3a14 60%,#5a8a2a)"></div><div class="venue__text"><div class="venue__name">Burger Ridge</div><div class="venue__kind">Americian</div></div><svg class="venue__go" width="12" height="18" viewBox="0 0 12 18"><path d="M2 2l8 7-8 7" fill="none" stroke="#999" stroke-width="3"/></svg></div>
  <div class="venue" style="top:320px"><div class="venue__thumb" role="img" aria-label="Photo d'une pièce de viande" style="background:linear-gradient(135deg,#7a2a1e,#c8705a 60%,#4a7a2a)"></div><div class="venue__text"><div class="venue__name">Steak House</div><div class="venue__kind">American</div></div><svg class="venue__go" width="12" height="18" viewBox="0 0 12 18"><path d="M2 2l8 7-8 7" fill="none" stroke="#999" stroke-width="3"/></svg></div>
  <div class="venue" style="top:396px"><div class="venue__thumb" role="img" aria-label="Photo d'une assiette de spaghetti" style="background:radial-gradient(circle,#b8321e,#e8d0b0 70%)"></div><div class="venue__text"><div class="venue__name">Spaghetti</div><div class="venue__kind">Italien</div></div><svg class="venue__go" width="12" height="18" viewBox="0 0 12 18"><path d="M2 2l8 7-8 7" fill="none" stroke="#999" stroke-width="3"/></svg></div>
  <div class="venue" style="top:472px"><div class="venue__thumb" role="img" aria-label="Photo de vin et fromage" style="background:linear-gradient(135deg,#3a2a1c,#9b7a3a)"></div><div class="venue__text"><div class="venue__name">Dolce Maria</div><div class="venue__kind">Italien</div></div><svg class="venue__go" width="12" height="18" viewBox="0 0 12 18"><path d="M2 2l8 7-8 7" fill="none" stroke="#999" stroke-width="3"/></svg></div>
  <div class="venue" style="top:548px"><div class="venue__thumb" role="img" aria-label="Photo de vin et fromage" style="background:linear-gradient(135deg,#3a2a1c,#9b7a3a)"></div><div class="venue__text"><div class="venue__name">Dolce Maria</div><div class="venue__kind">Italien</div></div><svg class="venue__go" width="12" height="18" viewBox="0 0 12 18"><path d="M2 2l8 7-8 7" fill="none" stroke="#999" stroke-width="3"/></svg></div>

  <nav class="tabbar">
    <div class="tab tab--active"><svg width="30" height="30" viewBox="0 0 30 30" fill="none" stroke="currentColor" stroke-width="2"><circle cx="18" cy="11" r="8"/><path d="M12 17L4 26"/></svg>Chercher</div>
    <div class="tab"><svg width="34" height="30" viewBox="0 0 34 30" fill="none" stroke="currentColor" stroke-width="2"><path d="M5 18a12 10 0 0 1 24 0zM2 21h30M17 6v2"/></svg>Commandes</div>
    <div class="tab"><svg width="30" height="30" viewBox="0 0 30 30" fill="none" stroke="currentColor" stroke-width="2"><rect x="4" y="6" width="22" height="19" rx="3"/><path d="M4 12h22M18 17h5"/></svg>Compte</div>
  </nav>
</section>

</body>
</html>
```